Tierkommunikation
Zielgruppe
Mittels Tierkommunikation vermittele ich bei Problemen oder Fragen zwischen Tier und Mensch.egal welche Rasse von Tier,bei mir kommt jedes Tier zu Wort!
Zielgruppe:alle Menschen die sich ein besseres Miteinander zwischen Tier und Mensch wünschen...
Aufgabenstellung
Es besteht bereits ein Bild von einem Pferd,welches ich gerne in das Design integrieren würde.
Pferd sollte das Auge Blau haben und ohne Halfter zu sehen sein. Farbe der Karte sollte in Anlehnung meiner Homepage gestaltet sein.http://www.pfotenbruecke-halmstett.com/#!was-ist-tk/c1uv3
Desweiteren wünsche ich mir den Text: Tierkommunikatorin, meinen Namen Telefonnummer und Homepage

```html
<!DOCTYPE html>
<html lang="de">
<head>
<meta charset="utf-8">
<title>Visitenkarte – Tierkommunikatorin</title>
<link rel="stylesheet" href="https://fonts.googleapis.com/css2?family=Tinos&family=Parisienne&display=swap">
<style>
  :root {
    --page: #ffffff;
    --card-cream: #f7f0e7;
    --card-back: #a0877a;
    --text-brown: #a08575;
    --accent-green: #b5cc3f;
    --horse-light-a: #d9cbb8;
    --horse-light-b: #b49c80;
    --horse-dark-a: #b08660;
    --horse-dark-b: #96735a;
    --shadow: rgba(0, 0, 0, 0.22);
  }
  * { margin: 0; padding: 0; box-sizing: border-box; }
  html, body {
    width: 1200px; height: 420px; overflow: hidden;
    background: var(--page);
  }
  .sheet { position: relative; width: 1200px; height: 420px; }
  .card {
    position: absolute; width: 541px; height: 349px; overflow: hidden;
    box-shadow: 8px 10px 18px var(--shadow);
  }
  .card--front { left: 33px; top: 22px; background: var(--card-cream); }
  .card--back { left: 616px; top: 25px; background: var(--card-back); }

  .title-rule { position: absolute; top: 39px; width: 107px; height: 8px; }
  .title-rule--left { left: 17px; }
  .title-rule--right { left: 412px; }

  .name {
    position: absolute; left: 0; right: 0; top: 17px;
    text-align: center;
    font-family: "Tinos", "Times New Roman", serif;
    font-weight: 400;
    font-size: 44px; line-height: 1; color: var(--text-brown);
  }
  .role {
    position: absolute; left: 0; right: 0; top: 52px;
    text-align: center;
    font-family: "Parisienne", cursive;
    font-size: 46px; line-height: 1.2; color: var(--accent-green);
  }
  .contact {
    position: absolute; right: 21px; top: 205px;
    text-align: right;
    font-family: "Tinos", "Times New Roman", serif;
    font-style: normal; font-weight: 400;
    font-size: 16px; line-height: 21.5px; color: var(--text-brown);
  }
  .contact p { white-space: nowrap; }
  .contact .gap { height: 21.5px; }

  .horse-art { position: absolute; }
  .horse-art--front {
    left: 0; top: 145px; width: 226px; height: 204px;
    background: radial-gradient(ellipse at 55% 55%, var(--horse-light-a) 0%, var(--horse-light-b) 70%, rgba(180,156,128,0.4) 100%);
    border-radius: 45% 55% 0 0 / 40% 60% 0 0;
  }
  .horse-art--back {
    left: 0; top: 55px; width: 320px; height: 294px;
    background: radial-gradient(ellipse at 55% 55%, var(--horse-dark-a) 0%, var(--horse-dark-b) 70%, rgba(160,135,122,0.5) 100%);
    border-radius: 45% 55% 0 0 / 40% 60% 0 0;
  }
</style>
</head>
<body>
<main class="sheet">
  <section class="card card--front" aria-label="Vorderseite">
    <svg class="title-rule title-rule--left" viewBox="0 0 107 8" aria-hidden="true">
      <line x1="22" y1="1" x2="107" y2="1" stroke="#a08575" stroke-width="1"/>
      <line x1="0" y1="7" x2="107" y2="7" stroke="#a08575" stroke-width="1"/>
    </svg>
    <svg class="title-rule title-rule--right" viewBox="0 0 107 8" aria-hidden="true">
      <line x1="0" y1="1" x2="85" y2="1" stroke="#a08575" stroke-width="1"/>
      <line x1="0" y1="7" x2="107" y2="7" stroke="#a08575" stroke-width="1"/>
    </svg>
    <h1 class="name">Maren Köhler</h1>
    <p class="role">Tierkommunikatorin</p>
    <div class="horse-art horse-art--front" role="img" aria-label="Aquarellzeichnung eines Pferdekopfes mit langer Mähne und blauem Auge in Sepiatönen"></div>
    <address class="contact">
      <p>Birkenweiler</p>
      <p>77999 Halmstett</p>
      <div class="gap"></div>
      <p>0151 23456789</p>
      <p>marenkoehler@beispielmail.de</p>
      <p>www.pfotenbruecke-halmstett.com</p>
    </address>
  </section>

  <section class="card card--back" aria-label="Rückseite">
    <div class="horse-art horse-art--back" role="img" aria-label="Große, getönte Aquarellzeichnung eines Pferdekopfes mit wehender Mähne und blauem Auge"></div>
  </section>
</main>
</body>
</html>
```